Flyer Design Project

Lanterns of Yore is a new collaborative of non-profit historical sites in the Greater Boston area. We're promoting the soft launch of our website by hosting open houses at each of the sites on September 21. We need a flyer to post up at each of the sites.

I have more print design needs to follow, and would really like to have a consistent look, so I intend to directly invite the winning designer to more projects.

Industry/Entity Type

Non-Profit

Requirements
Must have
• The flyer must be one page and be delivered as two files in Microsoft Publisher OR Microsoft Word. One file is for an 8 1/2 x 11 and one is as an 11 x 17 (same design, just scaled larger to fit the bigger paper).

It must have the Lanterns of Yore Logo (attached), and this text (attached) and use black font.

Any color that is not black or white must be chosen from these colors-but don't feel you have to use all of them:

Lanterns of Yore Website Colors

poppy red
c 0
m 93
y 87
k 0
web FF3333

nectarine
c 0
m 54
y 74
k 0
web FF9966

monaco blue

c 100
m 79
y 28
k 12
web 003366

tender shoots
c 30
m 0
y 89
k 0
web CCCC33

emerald
c 80
m 11
y 56
k 0
web 009999

african violet
c 28
m 44
y 0
k 0

web CC99CC

sunflower
c 10
m 33
y 99
k 0
web FF9933

lemon zest
c 4
m 13
y 77
k 0
web FFCC66

Nice to have
• Text and images with in the flyer should be large, simple and clear-as easy to see and read when the entire flyer is viewed on a mobile phone or from a distance as possible.

```html
<!DOCTYPE html>
<html lang="en">
<head>
<meta charset="utf-8">
<title>Lanterns of Yore – Open Houses</title>
<link rel="stylesheet" href="https://fonts.googleapis.com/css2?family=Source+Sans+3:wght@400;600;700&family=Lobster&family=Crimson+Pro:wght@400&display=swap">
<style>
  :root {
    --page: #ffffff;
    --blue: #1d5ea8;
    --blue-deep: #154f93;
    --blue-tile: #2a6bb4;
    --blue-tile-alt: #1a58a0;
    --monaco: #003366;
    --nectarine: #f7892a;
    --paper: #eceef1;
    --ink: #111111;
    --white: #ffffff;
    --arrow: #3fa6e6;
  }
  * { box-sizing: border-box; margin: 0; padding: 0; }
  html, body { width: 882px; height: 1200px; overflow: hidden; background: var(--page); }
  .flyer {
    position: relative; width: 882px; height: 1200px; background: var(--page);
    font-family: "Source Sans 3", Arial, sans-serif;
  }
  .backdrop {
    position: absolute; left: 12px; top: 290px; width: 846px; height: 888px;
    background: linear-gradient(180deg, var(--blue) 0%, var(--blue-deep) 100%);
  }
  .paper-panel {
    position: absolute; left: 518px; top: 714px; width: 340px; height: 464px;
    background: var(--paper);
  }
  .hero {
    position: absolute; left: 12px; top: 50px; width: 846px; height: 240px;
    background: linear-gradient(180deg, #8cc4ec 0%, #b9d7ea 38%, #6f8f4a 52%, #2f7fc4 66%, #1f66b0 100%);
  }
  .hero-title {
    position: absolute; left: 506px; top: 150px;
    font-family: "Lobster", cursive; font-size: 104px; line-height: 1;
    color: #e8f1fb; letter-spacing: 1px;
  }
  .tile { position: absolute; }
  .tile.photo { background: linear-gradient(160deg, #6f8a5a, #3c4f38); }
  .tile.plain { background: var(--blue-tile); }
  .tile.plain.alt { background: var(--blue-tile-alt); }
  .info-box {
    position: absolute; left: 30px; top: 522px; width: 298px; height: 296px;
    background: rgba(236, 240, 246, 0.9); border-radius: 10px;
    padding: 14px 16px 0 18px; color: var(--ink);
  }
  .info-box h2 {
    font-size: 23px; font-weight: 700; color: var(--nectarine); line-height: 1.1; margin-bottom: 4px;
  }
  .info-box p { font-size: 15.2px; line-height: 1.2; }
  .callout {
    position: absolute; left: 34px; top: 838px; width: 470px; height: 302px;
    background: rgba(90, 150, 215, 0.45); border-radius: 12px;
    padding: 10px 12px 0 10px;
  }
  .callout h2 {
    font-size: 25px; font-weight: 700; color: var(--nectarine); margin: 0 0 4px 16px; line-height: 1.1;
  }
  .callout ul { list-style: none; }
  .callout li {
    position: relative; padding-left: 28px; color: var(--white);
    font-size: 14.2px; line-height: 18.1px;
  }
  .callout li svg { position: absolute; left: 0; top: 4px; }
  .callout li.cont { padding-left: 28px; }
  .brand {
    position: absolute; left: 536px; top: 1040px; display: flex; align-items: center; gap: 16px;
  }
  .brand-mark { width: 64px; height: 64px; background: var(--monaco); border-radius: 50%; }
  .brand-name {
    font-family: "Source Sans 3", Arial, sans-serif; font-weight: 400;
    font-size: 46px; line-height: 46px; color: var(--monaco);
  }
</style>
</head>
<body>
<main class="flyer">
  <div class="hero" role="img" aria-label="City skyline over the river with sailboats and autumn trees"></div>
  <h1 class="hero-title">Boston</h1>

  <div class="backdrop"></div>
  <div class="paper-panel"></div>

  <div class="tile plain" style="left:184px;top:290px;width:160px;height:112px"></div>
  <div class="tile plain alt" style="left:518px;top:290px;width:158px;height:112px"></div>
  <div class="tile plain alt" style="left:344px;top:402px;width:174px;height:100px"></div>
  <div class="tile plain" style="left:676px;top:402px;width:182px;height:100px"></div>
  <div class="tile plain" style="left:518px;top:502px;width:158px;height:104px"></div>
  <div class="tile plain alt" style="left:676px;top:606px;width:182px;height:108px"></div>

  <div class="tile photo" style="left:12px;top:290px;width:172px;height:112px;background:linear-gradient(180deg,#1c2c4a,#6a4a2a)" role="img" aria-label="Historic brick mansion lit at dusk"></div>
  <div class="tile photo" style="left:344px;top:290px;width:174px;height:88px;background:linear-gradient(180deg,#c9c7d6,#6f8a52)" role="img" aria-label="Granite monument on a grassy hill"></div>
  <div class="tile photo" style="left:676px;top:290px;width:182px;height:112px;background:linear-gradient(160deg,#8fb0d8,#c9b27c 55%,#4f7a34)" role="img" aria-label="Colonial meeting house with white steeple"></div>
  <div class="tile photo" style="left:184px;top:402px;width:160px;height:96px;background:linear-gradient(160deg,#7ea35a,#3b5a2c)" role="img" aria-label="Cemetery with iron fence under green trees"></div>
  <div class="tile photo" style="left:518px;top:402px;width:158px;height:96px;background:linear-gradient(160deg,#a9c7e8,#d68aa6 40%,#b89a4c 70%,#5c7f36)" role="img" aria-label="Yellow house with flowering tree"></div>
  <div class="tile photo" style="left:344px;top:502px;width:174px;height:104px;background:linear-gradient(135deg,#3a7f9c,#9a3a2a 50%,#2e2e3a)" role="img" aria-label="Stained glass window with star pattern"></div>
  <div class="tile photo" style="left:676px;top:502px;width:182px;height:104px;background:linear-gradient(160deg,#8aa6c4,#6a6a5c 45%,#5f8a3a)" role="img" aria-label="Stone church with arched red door"></div>
  <div class="tile photo" style="left:518px;top:606px;width:158px;height:108px;background:linear-gradient(180deg,#5a7ab8,#2a2a2e 55%,#c88a4a)" role="img" aria-label="Round pavilion lit at night"></div>
  <div class="tile photo" style="left:678px;top:714px;width:176px;height:104px;background:linear-gradient(180deg,#3a3a5a,#2a4a9a 60%,#c9a24a)" role="img" aria-label="Cable-stayed bridge lit in blue at night"></div>

  <section class="info-box">
    <h2>Saturday, September 21</h2>
    <p>Columbus. Pilgrims. Revolution. Civil War. Industrialization.You know the history. But do you know the stories? Have you found how YOU are connected to the places and lives of the people who’ve shaped our world, our country, our state, and your life today? Find out by exploring some of Massachusetts’ treasured historical gems—you’ll be surprised by the wealth you discover.<br>For hours, directions, and discount/prize passes learn more at www.lanternsofyore.org</p>
  </section>

  <section class="callout">
    <h2>Call Out Box:</h2>
    <ul>
      <li><svg width="18" height="10" viewBox="0 0 18 10"><path d="M0 0 L18 5 L0 10 L5 5 Z" fill="var(--arrow)"/></svg>Special Tours, Games, Prizes, and Children’s Activities!</li>
      <li><svg width="18" height="10" viewBox="0 0 18 10"><path d="M0 0 L18 5 L0 10 L5 5 Z" fill="var(--arrow)"/></svg>Participating Organizations (must appear exactly as printed</li>
      <li class="cont">in the order listed)</li>
      <li><svg width="18" height="10" viewBox="0 0 18 10"><path d="M0 0 L18 5 L0 10 L5 5 Z" fill="var(--arrow)"/></svg>Harbor Rise at Linden Estate</li>
      <li><svg width="18" height="10" viewBox="0 0 18 10"><path d="M0 0 L18 5 L0 10 L5 5 Z" fill="var(--arrow)"/></svg>"Church of the Elders" Second Common Parish (Unitarian) of Marlow</li>
      <li><svg width="18" height="10" viewBox="0 0 18 10"><path d="M0 0 L18 5 L0 10 L5 5 Z" fill="var(--arrow)"/></svg>Ashcombe Memorial Library</li>
      <li><svg width="18" height="10" viewBox="0 0 18 10"><path d="M0 0 L18 5 L0 10 L5 5 Z" fill="var(--arrow)"/></svg>Elena Varga Dance Theatre's Home at Old Riverside Chapel</li>
      <li><svg width="18" height="10" viewBox="0 0 18 10"><path d="M0 0 L18 5 L0 10 L5 5 Z" fill="var(--arrow)"/></svg>Pennock's Boat Shop and Museum</li>
      <li><svg width="18" height="10" viewBox="0 0 18 10"><path d="M0 0 L18 5 L0 10 L5 5 Z" fill="var(--arrow)"/></svg>Mount Hazel Cemetery</li>
      <li><svg width="18" height="10" viewBox="0 0 18 10"><path d="M0 0 L18 5 L0 10 L5 5 Z" fill="var(--arrow)"/></svg>Heritage Museum of Black New England: Boston Campus</li>
      <li><svg width="18" height="10" viewBox="0 0 18 10"><path d="M0 0 L18 5 L0 10 L5 5 Z" fill="var(--arrow)"/></svg>Heritage Museum of Black New England: Nantucket Campus</li>
      <li><svg width="18" height="10" viewBox="0 0 18 10"><path d="M0 0 L18 5 L0 10 L5 5 Z" fill="var(--arrow)"/></svg>National Monument to the Settlers</li>
      <li><svg width="18" height="10" viewBox="0 0 18 10"><path d="M0 0 L18 5 L0 10 L5 5 Z" fill="var(--arrow)"/></svg>Old Keel Meeting House</li>
    </ul>
  </section>

  <div class="brand">
    <div class="brand-mark"></div>
    <div class="brand-name">Lanterns<br>of Yore</div>
  </div>
</main>
</body>
</html>
```